Spiritual Self-Help Book Cover: The Path of RISING the Heart Weaver

I’m looking for a powerful, eye-catching, and soulfully designed book cover for my upcoming spiritual self-help book titled: “The Path of RISING the Heart Weaver: A Quiet Path of Finding Your Voice, Honoring Your Flame, and Living Your Calling.” by Mira Holtby

Trim size: 6 x 9 inches (15.24 x 22.86 cm), full wrap cover including front, back, and spine.

This book is for spiritually awakening readers who are navigating inner transformation and want to reclaim their truth and power. The word BECOMING should stand out the most in the title design, as this is the central theme of the book — it’s a journey of evolution and embodiment.
I'm looking for a design that feels expansive, sacred, mystical, and empowering, with a tone that blends feminine spiritual energy with grounded strength. It should appeal to those interested in energy healing, light language, emotional alchemy, and soul purpose.

Design elements can include things like light, energy fields, sacred geometry, cosmic or mystical elements, or anything that visually conveys transformation, inner alchemy, or divine remembrance. Nothing too dark or overly esoteric — it should feel inspiring and elevated.
The final book will be available in print and ebook formats, so the design needs to be high resolution and adaptable.

Design Inspirations / Visual Keywords:
I’m drawn to covers that evoke a sense of spiritual awakening, inner transformation, and cosmic remembrance. Some elements I love include:
- Light bursts, energy waves, sacred geometry, subtle gold or white light effects
- Ethereal yet grounded designs (think: not overly abstract, but mystical and refined)
- Fonts that feel elevated, clean, and spacious, not overly bold or rigid
Please avoid designs that feel too dark, heavy, overly masculine, or sci-fi. I want the reader to feel empowered, uplifted, and activated the moment they see the cover.
- Final deliverables must include the original editable source file—preferably PSD (Photoshop)—so I can make future updates, including a German version of the book.

Back Cover Copy:
You were never broken—only buried beneath the layers of who you thought you had to be.
The Path of RISING the Heart Weaver is not just a book—it’s a sacred activation. A companion for the seeker who’s always felt like there was more. A map for those who are ready to transcend limitation, shed old identities, and reclaim the radiance of their true essence.
This isn’t about becoming something new. It’s about remembering what has always lived within you.
Through powerful transmissions, energetic teachings, and soul-deep reflection, you’ll be guided to awaken your inner Soul Alchemist—the version of you who lives in deep integrity with your truth, leads from embodied frequency, and walks as a living portal for transformation.
If you’ve felt the call to step into a higher path, this is your invitation.
The alchemical path awaits.

About the Author:
Mira Holtby is a Soul Alchemist, Light Language Channel, and transformational guide for awakening souls on the path of ascension and embodiment. Through her transmissions, activations, and deeply alchemical teachings, she supports others in dissolving limitations and becoming the living transmission of their soul’s truth. Her work empowers others to become the Soul Alchemist of their own life—fully awakened, energetically aligned, and consciously creating their reality from within.

Spine Text:
The Path of RISING the Heart Weaver Mira Holtby

Other Notes:
Please ensure the back cover layout includes space for:
• Barcode (bottom right or bottom center, standard placement)
• Optional decorative accents that match the front cover design
• Flow and visual balance across the full wrap (front + spine + back)

I uploaded a AI generated image that really captures the energy and feeling I’m going for—vibrant, mystical, intuitive, radiant, and feminine. I’m looking for designs that evoke soul embodiment, sacred transformation, and energetic activation like this. Please feel free to explore similar colors and tones.

Target Market(s)

Spiritually awakening women (and men) ages 30–55 who are seeking deeper truth, emotional healing, energetic expansion, and soul embodiment. They’re interested in spiritual growth, light language, quantum manifestation, energy work, and the journey of becoming their highest self.

Industry/Entity Type

Books / Publishing / Spirituality / Personal Development

Font styles to use
Serif
Script

Colors
A7469A
B969AE
D3A5CF
EDDBEB
F8F0F9
6B429C
8869AF
B7A5CE
E3DAEB
F3F0F8

Requirements
Must have
• Title: The Path of RISING the Heart Weaver (The word BECOMING should visually stand out the most) Subtitle: A Sacred Journey of Reclaiming Your Power, Remembering Your Light, and Embodying Your Truth. Author name Mira Holtby. Mystical yet grounded imagery (light, sacred geometry, ethereal elements) Energetic or spiritual theme (divine remembrance, embodiment, inner alchemy) High-resolution design adaptable for both print and ebook
Nice to have
• Subtle gold, white, or light-infused accents Cosmic or celestial textures (not heavy space imagery, but gently divine) Feminine and refined feel (without being overly soft or passive) A sense of spaciousness and radiance
Should not have
• Designs that feel dark, heavy, harsh, or overly masculine Sci-fi or overly abstract illustrations Bold, rigid fonts or clunky layout Imagery that feels disconnected from emotional or spiritual resonance

```html
<!DOCTYPE html>
<html lang="en">
<head>
<meta charset="utf-8">
<title>The Path of RISING the Heart Weaver — Mira Holtby</title>
<link rel="stylesheet" href="https://fonts.googleapis.com/css2?family=Cormorant+Garamond:wght@500;600&family=EB+Garamond:ital,wght@1,400&display=swap">
<style>
  :root {
    --gold: #b08a3e;
    --ink: #1c1412;
    --peach: #f9c6ae;
    --cream: #fdf3c8;
    --rose: #efaec0;
    --lilac: #d6a4cf;
    --glow: #fff6cf;
    --art-warm: #f6c870;
  }
  * { margin: 0; padding: 0; box-sizing: border-box; }
  html, body {
    width: 821px;
    height: 1200px;
    overflow: hidden;
  }
  body { background: var(--peach); }
  .cover {
    position: relative;
    width: 821px;
    height: 1200px;
    overflow: hidden;
    background:
      radial-gradient(ellipse 260px 360px at 50% 33%, var(--glow) 0%, rgba(253,240,196,0.85) 35%, rgba(253,230,190,0) 100%),
      radial-gradient(ellipse 520px 300px at 50% 62%, rgba(252,224,170,0.75) 0%, rgba(252,224,170,0) 100%),
      radial-gradient(ellipse 300px 260px at 100% 0%, rgba(222,176,214,0.9) 0%, rgba(222,176,214,0) 100%),
      radial-gradient(ellipse 340px 300px at 100% 100%, rgba(208,160,214,0.95) 0%, rgba(208,160,214,0) 100%),
      radial-gradient(ellipse 320px 240px at 0% 100%, rgba(220,168,206,0.9) 0%, rgba(220,168,206,0) 100%),
      linear-gradient(180deg, #fbd7c0 0%, var(--peach) 45%, #f6b9ae 70%, var(--rose) 88%, var(--lilac) 100%);
  }
  .rays {
    position: absolute;
    inset: 0;
    width: 821px;
    height: 1200px;
  }
  .title-block {
    position: absolute;
    left: 0;
    right: 0;
    top: 88px;
    text-align: center;
    color: var(--gold);
    font-family: "Cormorant Garamond", Georgia, serif;
    font-weight: 600;
  }
  .title-lead {
    font-size: 56px;
    line-height: 1;
    letter-spacing: 2px;
  }
  .title-key {
    font-size: 128px;
    line-height: 1;
    letter-spacing: 4px;
    margin-top: 22px;
  }
  .title-tail {
    font-size: 54px;
    line-height: 1;
    letter-spacing: 4px;
    margin-top: 20px;
  }
  .subtitle {
    position: absolute;
    left: 0;
    right: 0;
    top: 378px;
    text-align: center;
    color: var(--ink);
    font-family: "EB Garamond", Georgia, serif;
    font-style: italic;
    font-size: 26px;
    line-height: 42px;
    letter-spacing: 0.5px;
  }
  .emblem {
    position: absolute;
    left: 205px;
    top: 596px;
    width: 420px;
    height: 412px;
    border-radius: 50%;
    background: radial-gradient(ellipse at 50% 55%, rgba(246,200,112,0.85) 0%, rgba(248,212,140,0.55) 45%, rgba(250,224,170,0) 72%);
  }
  .author {
    position: absolute;
    left: 0;
    right: 0;
    top: 1074px;
    text-align: center;
    color: var(--gold);
    font-family: "Cormorant Garamond", Georgia, serif;
    font-weight: 500;
    font-size: 57px;
    line-height: 1;
    letter-spacing: 3px;
  }
</style>
</head>
<body>
  <main class="cover">
    <svg class="rays" viewBox="0 0 821 1200" aria-hidden="true">
      <g stroke="#fff8d8" stroke-width="1" opacity="0.45">
        <line x1="410" y1="380" x2="410" y2="0"/>
        <line x1="410" y1="380" x2="250" y2="0"/>
        <line x1="410" y1="380" x2="570" y2="0"/>
        <line x1="410" y1="380" x2="80" y2="80"/>
        <line x1="410" y1="380" x2="740" y2="80"/>
        <line x1="410" y1="380" x2="40" y2="300"/>
        <line x1="410" y1="380" x2="780" y2="300"/>
        <line x1="410" y1="380" x2="120" y2="560"/>
        <line x1="410" y1="380" x2="700" y2="560"/>
        <line x1="410" y1="380" x2="300" y2="680"/>
        <line x1="410" y1="380" x2="520" y2="680"/>
      </g>
    </svg>

    <h1 class="title-block">
      <div class="title-lead">THE PATH OF</div>
      <div class="title-key">RISING</div>
      <div class="title-tail">THE HEART WEAVER</div>
    </h1>

    <p class="subtitle">
      A Quiet Path of Finding Your Voice,<br>
      Honoring Your Flame, and Living Your Calling
    </p>

    <div class="emblem" role="img" aria-label="Golden silhouette of a woman seated in meditation before a sacred geometry flower pattern crowned by a radiant star"></div>

    <p class="author">MIRA HOLTBY</p>
  </main>
</body>
</html>
```